Vegan Alfredo Sauce Label Design for Bramble Pantry Co

We are a food co. committed to making vegan food more accessible to people who want to eat healthier. Our first line of product is vegan Alfredo sauce.
We have 3 flavors:
- Garlic
- Pesto
- Lemony Artichoke
The current project is the design for the first flavor: garlic. However, we would like a template that would translate well to other flavors, so they look like a family of products.
These will be in standard 16 oz jars. The whole label will be approx 6cm x 24cm, but the front visual space is approx 6cm x 10cm. The rest will be nutritional labeling and copy about the company.
We also need a stamp or font- based logo that says Bramble Pantry Co. (or lower case: bramble pantry co.), the name of the company.
The picture (attached) of Vegan Mimbo is the closest to what we are going for. Because the sauce is creamy white, a colorful background with off-white font will be best.
We currently have a website, although we are doing a brand over-haul (hence, this posting) www.bramblepantryco-example.com. If the designer is a good fit, we have several more projects, in line.
Other brands we love: Tidy Acres, Marlow Ridge Foods, Pulp Poured Daily.
The final brand should communicate hip, natural and health.
And personally, I love design that is clever and somehow makes me smile.
Target Market(s)
Vegans, vegetarians, and people with common food allergies - all ages.
Young, hip families.
Industry/Entity Type
It Company
Requirements
Must have
- Copy:
Vegan Alfredo or Vegan Alfredo Sauce
Garlic
Bramble Pantry or Bramble Pantry Co
16 oz
Nice to have
- May include copy:
Gluten-Free Soy-Free Nut-Free
Should not have
- Neon colors

```html
<!DOCTYPE html>
<html lang="en">
<head>
<meta charset="utf-8">
<title>Bramble Pantry Co. – Vegan Alfredo Sauce Label</title>
<link href="https://fonts.googleapis.com/css2?family=Kaushan+Script&family=Playfair+Display:wght@700&family=Oswald:wght@300;400&family=Roboto+Condensed:wght@400;700&display=swap" rel="stylesheet">
<style>
:root{
  --brown-deep:#4a2d16;
  --brown:#6b4423;
  --brown-panel:#7a4c22;
  --gold:#c9973f;
  --gold-light:#e7c987;
  --parchment:#f1dfb8;
  --parchment-edge:#dcb978;
  --cream:#fbf0d3;
  --heading-gold:#f0c874;
  --carb:#d2683a;
  --protein:#4aa2b4;
  --fat:#e0cf5c;
  --ink:#222;
}
*{box-sizing:border-box;margin:0;padding:0}
html,body{width:1200px;height:300px;overflow:hidden;background:#fff}
.label{position:relative;width:1200px;height:300px;overflow:hidden;
  background:radial-gradient(ellipse at 50% 45%,var(--parchment) 0%,#e8cc90 45%,var(--gold) 100%);
  font-family:"Roboto Condensed",Arial,sans-serif}
.label__back{position:absolute;left:0;top:0;width:405px;height:300px;
  background:linear-gradient(180deg,#d9aa55,#c08a35 60%,#d5a456)}
.label__side{position:absolute;right:0;top:0;width:395px;height:300px;
  background:linear-gradient(180deg,#e2bb70,#d4a452)}

/* story panel */
.story{position:absolute;left:38px;top:28px;width:348px;height:222px;background:var(--brown-panel);
  color:var(--cream);padding:6px 10px;font-size:8.4px;line-height:1.28}
.story h3{font-size:9px;color:var(--heading-gold);font-weight:700;margin-bottom:3px}
.story p{margin-bottom:5px}
.batch{display:grid;grid-template-columns:110px 46px;row-gap:2px;font-weight:700;margin:4px 0 5px;
  padding:3px 0;border-top:1px solid rgba(255,240,210,.4);border-bottom:1px solid rgba(255,240,210,.4);width:160px}
.batch span:nth-child(even){text-align:right}
.best{font-weight:700;font-size:8.8px;margin-bottom:6px}
.story .brand-name{font-family:"Playfair Display",serif;font-size:13px;color:var(--cream);margin:8px 0 3px;
  padding-top:5px;border-top:1px solid rgba(255,240,210,.4)}
.contact{position:absolute;left:38px;top:250px;width:348px;height:30px;background:var(--cream);
  color:var(--brown-deep);font-size:8.4px;text-align:center;line-height:1.25;padding-top:4px}

/* front */
.front{position:absolute;left:405px;top:0;width:395px;height:300px;text-align:center}
.ribbon{position:absolute;left:88px;top:8px;width:220px;height:38px}
.ribbon__shape{position:absolute;left:0;top:0;width:100%;height:100%}
.ribbon__text{position:absolute;left:0;right:0;top:4px;line-height:26px;font-family:"Playfair Display",serif;
  font-size:17px;color:var(--cream);white-space:nowrap}
.free-from{position:absolute;top:52px;width:100%;font-family:"Oswald",sans-serif;font-weight:400;
  font-size:11px;color:var(--brown);letter-spacing:.3px}
.free-from i{font-style:normal;margin:0 5px;opacity:.6}
.product-name{position:absolute;top:72px;width:100%;font-family:"Kaushan Script",cursive;font-size:56px;
  font-weight:400;color:var(--brown);line-height:1}
.product-type{position:absolute;top:154px;width:100%;font-family:"Oswald",sans-serif;font-weight:300;
  font-size:22px;line-height:1;letter-spacing:2px;color:var(--brown)}
.garlic-art{position:absolute;left:100px;top:180px;width:200px;height:82px;border-radius:45%;
  background:radial-gradient(ellipse at center,rgba(150,110,70,.45),rgba(150,110,70,0) 70%)}
.flavor-bar{position:absolute;left:28px;top:264px;width:340px;height:24px;background:var(--brown);
  display:flex;justify-content:space-between;align-items:center;padding:0 24px;
  font-family:"Oswald",sans-serif;font-weight:300;font-size:14px;letter-spacing:2px;color:var(--cream)}

/* side info */
.info{position:absolute;left:833px;top:22px;width:182px;height:183px;background:var(--brown-panel);
  color:var(--cream);padding:5px 8px;font-size:8.2px;line-height:1.28}
.info h3{color:var(--heading-gold);font-size:8.8px;font-weight:700;margin:2px 0 3px}
.info p{margin-bottom:4px;text-align:justify}
.calories{position:absolute;left:833px;top:210px;width:182px;height:70px;background:var(--cream);padding:4px 8px}
.calories h3{font-size:10px;color:var(--carb);font-weight:700}
.legend{list-style:none;font-size:8.6px;color:#333;margin-top:4px;line-height:1.55}
.legend li::before{content:"";display:inline-block;width:7px;height:7px;border-radius:50%;margin-right:5px;background:var(--c)}
.pie{position:absolute;right:6px;top:5px;width:60px;height:60px;transform:rotate(-90deg)}

.facts{position:absolute;left:1022px;top:22px;width:138px;height:258px;background:#fff;color:var(--ink);
  padding:3px 5px;font-size:6.6px;line-height:1.25}
.facts h2{font-family:"Roboto Condensed",sans-serif;font-size:15px;font-weight:700;line-height:1.1;
  border-bottom:1px solid #333;padding-bottom:1px}
.facts .row{display:flex;justify-content:space-between;border-bottom:.5px solid #999;padding:1.4px 0}
.facts .b{font-weight:700}
.facts .thick{border-bottom:2px solid #333}
.facts .note{background:#bdbdbd;color:#fff;text-align:center;font-size:6.6px;margin:3px -5px 0;padding:2px}
</style>
</head>
<body>
<div class="label">
  <div class="label__back"></div>
  <div class="label__side"></div>

  <section class="story">
    <h3>Our Story:</h3>
    <p>Lorem ipsum,andit sem sit amet viverra cursus. Ut metus sem, luctus a nibh nec, interdum consequat risus. Cum sociis natoque penatibus et magnis dis parturient montes, nascetur ridiculus mus. Etiam consectetur mattis leo id auctor.</p>
    <p>t sem sit amet viverra cursus. Ut metus sem, luctus a nibh nec, interdum consequat risus. Cum sociis natoque penatibus et magnis dis parturient montes, nascetur ridiculus mus. Etiam consectetur mattis leo id auctor.</p>
    <div class="batch">
      <span>Batch No :</span><span>4343w</span>
      <span>Mfg Date :</span><span>00 Aug 0000</span>
      <span>MRP (inclusive of all taxes):</span><span>$00.0</span>
    </div>
    <p class="best">Best before 00 months from the date of manufacturing</p>
    <h3 class="brand-name">Bramble Pantry Co.</h3>
    <p>Lorem ipsum, Dolor sit amet, consectetur, Adipiscing elit, amet viverra cursus. Ut metus sem, luctus a nibh nec, interdum consequat risus.</p>
  </section>
  <div class="contact">For any product related query please contact: 555 014 2290<br>email us: hello@bramblepantryco-example.com</div>

  <section class="front">
    <div class="ribbon">
      <svg class="ribbon__shape" viewBox="0 0 220 38" aria-hidden="true">
        <polygon points="0,10 22,10 22,34 0,34 8,22" fill="#4a2d16"/>
        <polygon points="220,10 198,10 198,34 220,34 212,22" fill="#4a2d16"/>
        <rect x="14" y="4" width="192" height="26" fill="#6b4423"/>
      </svg>
      <span class="ribbon__text">Bramble Pantry Co.</span>
    </div>
    <div class="free-from">GLUTEN FREE<i>|</i>SOY FREE<i>|</i>NUT FREE</div>
    <h1 class="product-name">Vegan Alfredo</h1>
    <div class="product-type">SAUCE</div>
    <div class="garlic-art" role="img" aria-label="Sketch of garlic bulbs and cloves"></div>
    <div class="flavor-bar"><span>GARLIC</span><span>16 OZ</span></div>
  </section>

  <section class="info">
    <h3>Ingredients:</h3>
    <p>Lorem ipsum, Dolor sit amet, consectetur, Adipiscing elit.</p>
    <h3>Directions for use:</h3>
    <p>Sed blandit sem sit amet viverra cursus. Ut metus sem, luctus a nibh nec, interdum consequat risus. Cum sociis natoque penatibus et magnis dis parturient montes, nascetur ridiculus mus. Etiam consectetur mattis leo id auctor.</p>
    <h3>Storage:</h3>
    <p>Donec a condimentum velit. Proin sed sagittis eros. Phasellus varius elit sit amet mi tincidunt pulvinar. Cras dictum suscipit enim, ut accumsan neque pharetra et.</p>
  </section>

  <section class="calories">
    <h3>Calorie Breakdown:</h3>
    <ul class="legend">
      <li style="--c:var(--carb)">Carbohydrate (25.5%)</li>
      <li style="--c:var(--protein)">Protein (63.75%)</li>
      <li style="--c:var(--fat)">Fat (10.75%)</li>
    </ul>
    <svg class="pie" viewBox="0 0 42 42" aria-label="Pie chart of calorie breakdown">
      <circle r="10.5" cx="21" cy="21" fill="none" stroke="var(--carb)" stroke-width="21" pathLength="100" stroke-dasharray="25.5 100"/>
      <circle r="10.5" cx="21" cy="21" fill="none" stroke="var(--protein)" stroke-width="21" pathLength="100" stroke-dasharray="63.75 100" stroke-dashoffset="-25.5"/>
      <circle r="10.5" cx="21" cy="21" fill="none" stroke="var(--fat)" stroke-width="21" pathLength="100" stroke-dasharray="10.75 100" stroke-dashoffset="-89.25"/>
    </svg>
  </section>

  <section class="facts">
    <h2>Nutrition Facts</h2>
    <div>Serving Size: 1 teaspoon (0g)</div>
    <div>Serving Per Container: 00</div>
    <div class="thick">Amount Per Serving</div>
    <div class="row b"><span>Calories 0</span><span>Calories from Fat 0</span></div>
    <div class="row b thick" style="justify-content:flex-end"><span>% Daily Value*</span></div>
    <div class="row b"><span>Total Fat 0g</span><span>0%</span></div>
    <div class="row"><span>Saturated Fat 0g</span><span>0%</span></div>
    <div class="row"><span>Trans Fat 0g</span><span>0%</span></div>
    <div class="row"><span>Cholesterol 0mg</span><span>0%</span></div>
    <div class="row"><span>Sodium 0mg</span><span>0%</span></div>
    <div class="row b"><span>Total Carbohydrate 0g</span><span>0%</span></div>
    <div class="row"><span>Dietary Fiber 0g</span><span>0%</span></div>
    <div class="row"><span>Sugars</span><span>0g</span></div>
    <div class="row b thick"><span>Protein 0g</span><span>0%</span></div>
    <div class="row"><span>Vitamin A</span><span>0%</span></div>
    <div class="row"><span>Vitamin C</span><span>0%</span></div>
    <div class="row"><span>Calcium</span><span>0%</span></div>
    <div class="row"><span>Iron</span><span>0%</span></div>
    <div class="note">Percent Daily Values are based on<br>a 2000 calorie diet.</div>
  </section>
</div>
</body>
</html>
```